Weight loss surgery restaurant card

We need to create a card for patients who have undergone weight loss surgery to take to restaurants so they can request smaller meals. These patients have had surgery on their stomach so that they can only consume half to one cup of food at a time. So normal sized restaurant meals are way too big (and cost a lot). This card they can present to the restaurant to communicate the fact that they have had weight loss surgery and therefore request a smaller meal portion at reduced cost

Target Market(s)

Restaurants serving weight loss surgery patients

Industry/Entity Type

Health Care

Contact Information for Business Card

This will be a plastic card similar to business card size.

Requirements
Must have
• The front of the card should include the following text:
• The individual bearing this card has undergone weight loss surgery.
• This surgery restricts portion sizes to between half and one cup of food at a time.
• Please give consideration to allowing smaller portions of your regular meals to be ordered to reduce wastage and excess costs.
• Example: a half size portion priced at two thirds of usual cost.
• The back of the card will have spaces for the person to write certain information. These are the categories that can be filled in by hand:
• Name:
• Procedure performed:
• Date of procedure (month/year):
• Treating Clinic Name:
• Treating Clinic Signature:
• Somewhere down the bottom should be something along the lines of:
• supplied from marcuswheelan.com.au
Nice to have
• A nice design with imagery/colours etc ... not just the text on a white background! Bright attractive colours preferred.
• I have uploaded my logo ... a roughly triangular image followed by my name etc. The triangular logo image could be used somewhere on the card and this logo can be interchangeable for other clinics who purchase the card.
• **Please note that I don't want my name to be included as part of the logo on the card ... just use the triangular image on the side of the logo without the following name**
• Also, the colouring of the card does not have to reflect my logo colours as I am anticipating interchanging this logo with other logos if other clinics choose to adopt the card. I am interested to see other, more generic, colour choices as well as my logo colours

```html
<!DOCTYPE html>
<html lang="en">
<head>
<meta charset="utf-8">
<title>Weight Loss Surgery Restaurant Card</title>
<link rel="stylesheet" href="https://fonts.googleapis.com/css2?family=Roboto+Condensed:wght@400;700&family=Roboto:wght@400&family=Titillium+Web:wght@700&family=Cookie&family=Exo+2:wght@800&display=swap">
<style>
  :root {
    --page: #e9e5df;
    --maroon: #8e1a45;
    --maroon-text: #8a1c3f;
    --sky: #a9c7ea;
    --lemon: #f6e62c;
    --white: #ffffff;
    --rule: #9b3a8a;
    --line: #444;
    --food-a: #c9b48a;
    --food-b: #6f8a3e;
    --food-c: #e6ded0;
  }
  * { box-sizing: border-box; margin: 0; padding: 0; }
  html, body { width: 900px; height: 1200px; overflow: hidden; }
  body { background: var(--page); position: relative; font-family: "Roboto", sans-serif; }

  .card {
    position: absolute; left: 82px; width: 733px; height: 428px;
    border-radius: 22px; overflow: hidden;
    box-shadow: 0 6px 16px rgba(0,0,0,.25);
  }
  .card--front { top: 137px; background: var(--maroon); }
  .card--back  { top: 635px; background: var(--white); }

  .front-art { position: absolute; inset: 0; }

  .front-copy {
    position: absolute; right: 28px; top: 30px; width: 520px; text-align: right;
  }
  .headline {
    font-family: "Roboto Condensed", sans-serif; font-weight: 700;
    font-size: 28px; line-height: 33px; color: var(--white); letter-spacing: .3px;
  }
  .headline__accent { color: var(--sky); display: block; }
  .restriction {
    font-family: "Cookie", cursive; color: var(--lemon);
    font-size: 44px; line-height: 37.5px; margin-top: 20px;
  }
  .request {
    font-family: "Titillium Web", sans-serif; font-weight: 700;
    color: var(--white); font-size: 21.5px; line-height: 26px;
    margin-top: 22px;
  }
  .example {
    font-family: "Roboto Condensed", sans-serif; font-size: 17.5px;
    color: var(--sky); margin-top: 22px;
  }
  .example__label { color: var(--lemon); font-style: italic; font-weight: 700; font-size: 19px; margin-right: 4px; }

  .back-band {
    position: absolute; left: 0; right: 0;
    background: linear-gradient(90deg, var(--food-b), var(--food-a) 40%, var(--food-c) 70%, var(--food-b));
  }
  .back-band--top { top: 0; height: 27px; border-bottom: 1.5px solid var(--rule); }
  .back-band--bottom { bottom: 0; height: 48px; border-top: 1.5px solid var(--rule);
    display: flex; align-items: center; justify-content: center; }
  .back-body {
    position: absolute; left: 0; right: 0; top: 27px; bottom: 48px;
    background: linear-gradient(135deg, #f7f5f1, #efebe4 50%, #f6f3ee);
  }
  .supplier {
    font-family: "Exo 2", sans-serif; font-weight: 800; font-size: 20px;
    color: var(--white); letter-spacing: 1.6px; text-transform: uppercase;
    text-shadow: 0 1px 2px rgba(0,0,0,.45);
  }
  .clinic-mark {
    position: absolute; right: 52px; top: 52px;
    display: flex; align-items: center; gap: 6px;
    font-family: "Roboto", sans-serif; font-size: 15px; color: var(--maroon-text);
  }
  .clinic-mark__dot { width: 14px; height: 14px; border-radius: 50%; background: #2fa7a0; }

  .fields { position: absolute; left: 48px; right: 48px; top: 97px; }
  .field {
    display: flex; align-items: flex-end; height: 51px;
    color: var(--maroon-text); font-size: 15px;
  }
  .field__label { white-space: nowrap; padding-right: 8px; }
  .field__line { flex: 1; border-bottom: 1px solid var(--line); margin-bottom: 4px; }
</style>
</head>
<body>

<section class="card card--front" aria-label="Card front">
  <svg class="front-art" width="733" height="428" viewBox="0 0 733 428">
    <defs>
      <linearGradient id="dishes" x1="0" y1="0" x2="1" y2="1">
        <stop offset="0" stop-color="#7c8f45"/>
        <stop offset=".35" stop-color="#cfc19a"/>
        <stop offset=".65" stop-color="#b98a4d"/>
        <stop offset="1" stop-color="#6b4a35"/>
      </linearGradient>
    </defs>
    <path d="M322 0 C345 30 352 80 335 130 C310 200 250 240 222 300 C205 340 205 390 212 428 L232 428 C225 390 226 345 242 305 C270 245 332 205 356 132 C372 80 364 30 342 0 Z" fill="#ffffff"/>
    <path role="img" aria-label="Photo of shared dishes: stir-fried greens, hotpot broth and skewers on a table"
          d="M0 0 L322 0 C345 30 352 80 335 130 C310 200 250 240 222 300 C205 340 205 390 212 428 L0 428 Z" fill="url(#dishes)"/>
  </svg>

  <div class="front-copy">
    <h1 class="headline">THE INDIVIDUAL BEARING<br>THIS CARD HAS UNDERGONE
      <span class="headline__accent">WEIGHT LOSS SURGERY</span></h1>
    <p class="restriction">This surgery restricts<br>portion sizes to between half<br>and one cup of food at a time.</p>
    <p class="request">Please give consideration to allowing smaller<br>portions&nbsp; of your regular meals to be ordered to<br>reduce wastage and excess costs.</p>
    <p class="example"><span class="example__label">EXAMPLE:</span> a half size portion priced at two thirds of usual cost.</p>
  </div>
</section>

<section class="card card--back" aria-label="Card back">
  <div class="back-band back-band--top" role="img" aria-label="Strip of food photography"></div>
  <div class="back-body" role="img" aria-label="Faded photo of shared dishes behind the form"></div>

  <div class="clinic-mark"><span class="clinic-mark__dot"></span>Wheelan</div>

  <div class="fields">
    <div class="field"><span class="field__label">Name :</span><span class="field__line"></span></div>
    <div class="field"><span class="field__label">Procedure performed :</span><span class="field__line"></span></div>
    <div class="field"><span class="field__label">Date of procedure (month/year) :</span><span class="field__line"></span></div>
    <div class="field"><span class="field__label">Treating Clinic Name:</span><span class="field__line"></span></div>
    <div class="field"><span class="field__label">Treating Clinic Signature:</span><span class="field__line"></span></div>
  </div>

  <div class="back-band back-band--bottom">
    <p class="supplier">Meal cards available at marcuswheelan.com.au</p>
  </div>
</section>

</body>
</html>
```